Business Card Design Project for - The Pellowick Greenworks Company Ltd. We are a Landscape and garden

I would like designer to use all special glosses etc so i can have a professional looking business card. The theme of the business card can reflect that of the Logo attached by MarkQuarry or your own unique ideas.. please feel free to go wild as i hope i can select a winner i like - my budget will be committed so please get involved. Good luck and thank you Lyndon

Target Market(s)

Must look Professional

General Public and Businesses including Councils, Local Government, Hospitals, Hotels, Professionals and Professional Sports People.

Industry/Entity Type

Landscape Gardening

Contact Information for Business Card

The Pellowick Greenworks Company Ltd

Mr L.R Ashcombe
Head Office - Quayfront Park Manchester
t. 0772 408 916
e. info@pellowickgreenworks.co.uk
w. www.pellowickgreenworks.co.uk

Facebook - https://www.friendpage-example.com/ThePellowickGreenworksCompany/
Twitter - https://chirpline-example.com/ThePruningCart
Instagram - https://www.snapgrid-example.com/thepellowickgreenworkscompany/?hl=en
Google+ - https://circles.searchhub-example.com/u/0/208473950162438571093
Yelp - https://www.reviewnook-example.co.uk/biz/the-pellowick-greenworks-company-manchester-4

Font styles to use
Serif
Script
Other font styles liked:
• I don't have much of an idea of font types sorry

Colors

Designer to choose colors to be used in the design.

Requirements
Must have
• A Professional look and Design
• Special effects with gloss and fading of colours possibly..
• Front and back design
Nice to have
• All special features with effects and gloss etc

```html
<!DOCTYPE html>
<html lang="en">
<head>
<meta charset="utf-8">
<title>The Pellowick Greenworks Company Ltd – Business Card</title>
<link href="https://fonts.googleapis.com/css2?family=Cinzel:wght@500&family=Lato:wght@400&family=Oswald:wght@300;600&display=swap" rel="stylesheet">
<style>
  :root {
    --backdrop: #c9cccc;
    --card-dark: #111315;
    --card-mid: #23272a;
    --leaf-green: #5fc03c;
    --leaf-deep: #2f8f2a;
    --ink-light: #f1f3f2;
    --ink-muted: #cfd4d2;
    --silver-hi: #f4f5f5;
    --silver-lo: #9da2a3;
    --band-ink: #141516;
  }
  * { box-sizing: border-box; margin: 0; padding: 0; }
  html, body { width: 1200px; height: 1200px; overflow: hidden; }
  body {
    background: var(--backdrop);
    display: flex;
    align-items: center;
    justify-content: center;
    gap: 120px;
  }
  .card {
    position: relative;
    width: 420px;
    height: 720px;
    background:
      radial-gradient(ellipse at 70% 20%, rgba(255,255,255,0.07), transparent 60%),
      linear-gradient(160deg, var(--card-mid) 0%, var(--card-dark) 55%, #0b0c0d 100%);
    box-shadow: 0 18px 40px rgba(0,0,0,0.35);
    overflow: hidden;
  }
  .brand {
    display: flex;
    flex-direction: column;
    align-items: center;
    color: var(--ink-light);
    font-family: "Cinzel", serif;
    font-weight: 500;
    text-align: center;
  }
  .brand-mark {
    width: 54px; height: 54px;
    border-radius: 50%;
    background: radial-gradient(circle at 35% 30%, var(--leaf-green), var(--leaf-deep));
    margin-bottom: 14px;
  }
  .brand-name { font-size: 29px; letter-spacing: 2px; line-height: 1.1; }
  .brand-sub { font-size: 11.5px; letter-spacing: 3px; margin-top: 6px; color: var(--ink-light); }

  .card-front .brand { position: absolute; top: 62px; left: 0; right: 0; }

  .name-band {
    position: absolute;
    top: 296px; left: 0; right: 0;
    height: 60px;
    background: linear-gradient(180deg, var(--silver-hi) 0%, #c9cdce 45%, var(--silver-lo) 100%);
    display: flex; align-items: center; justify-content: center;
    font-family: "Oswald", sans-serif;
    font-weight: 600;
    font-size: 31px;
    letter-spacing: 0.5px;
    color: var(--band-ink);
  }

  .contact-list {
    position: absolute;
    top: 384px; left: 48px;
    list-style: none;
    font-family: "Lato", sans-serif;
    font-size: 16px;
    color: var(--ink-light);
  }
  .contact-list li { display: flex; align-items: center; height: 31px; }
  .contact-icon { width: 16px; height: 16px; margin-right: 16px; flex: none; }

  .social-list {
    position: absolute;
    top: 532px; left: 48px;
    list-style: none;
    font-family: "Oswald", sans-serif;
    font-weight: 300;
    font-size: 14.5px;
    color: var(--ink-muted);
  }
  .social-list li { display: flex; align-items: center; height: 32px; white-space: nowrap; }
  .social-dot {
    width: 19px; height: 19px; border-radius: 50%;
    background: var(--leaf-green);
    margin-right: 14px; flex: none;
  }

  .card-back .brand { position: absolute; top: 268px; left: 0; right: 0; }
  .card-back .brand-mark { width: 64px; height: 64px; }
  .card-back .brand-name { font-size: 32px; }
  .card-back .brand-sub { font-size: 12.5px; }
</style>
</head>
<body>

<section class="card card-front" aria-label="Business card front">
  <div class="brand">
    <span class="brand-mark"></span>
    <span class="brand-name">THE PELLOWICK</span>
    <span class="brand-sub">GREENWORKS COMPANY LTD</span>
  </div>

  <div class="name-band">MR L.R ASHCOMBE</div>

  <ul class="contact-list">
    <li>
      <svg class="contact-icon" viewBox="0 0 16 16"><path d="M8 1a5 5 0 0 0-5 5c0 3.8 5 9 5 9s5-5.2 5-9a5 5 0 0 0-5-5zm0 7a2 2 0 1 1 0-4 2 2 0 0 1 0 4z" fill="var(--leaf-green)"/></svg>
      Head Office - Quayfront Park Manchester
    </li>
    <li>
      <svg class="contact-icon" viewBox="0 0 16 16"><path d="M3.5 1.5l2.6-.4 1.3 3.2-1.7 1.3a8 8 0 0 0 4.2 4.2l1.3-1.7 3.2 1.3-.4 2.6c-.2.8-1 1.3-1.8 1.2C6.4 12.6 2.8 9 2.2 3.3c-.1-.8.4-1.6 1.3-1.8z" fill="var(--leaf-green)"/></svg>
      0772 408 916
    </li>
    <li>
      <svg class="contact-icon" viewBox="0 0 16 16"><rect x="1" y="3" width="14" height="10" rx="1" fill="var(--leaf-green)"/><path d="M1.5 3.8L8 9l6.5-5.2" stroke="var(--card-dark)" stroke-width="1.3" fill="none"/></svg>
      info@pellowickgreenworks.co.uk
    </li>
    <li>
      <svg class="contact-icon" viewBox="0 0 16 16" fill="none" stroke="var(--leaf-green)" stroke-width="1.4"><circle cx="8" cy="8" r="6.5"/><ellipse cx="8" cy="8" rx="2.8" ry="6.5"/><path d="M1.5 8h13M2.6 4.5h10.8M2.6 11.5h10.8"/></svg>
      www.pellowickgreenworks.co.uk
    </li>
  </ul>

  <ul class="social-list">
    <li><span class="social-dot"></span>/ThePellowickGreenworksCompany</li>
    <li><span class="social-dot"></span>chirpline-example.com/ThePruningCart</li>
    <li><span class="social-dot"></span>snapgrid-example.com/thepellowickgreenworkscompany</li>
    <li><span class="social-dot"></span>circles.searchhub-example.com/u/0/208473950162438571093</li>
    <li><span class="social-dot"></span>/the-pellowick-greenworks-company-manchester</li>
  </ul>
</section>

<section class="card card-back" aria-label="Business card back">
  <div class="brand">
    <span class="brand-mark"></span>
    <span class="brand-name">THE PELLOWICK</span>
    <span class="brand-sub">GREENWORKS COMPANY LTD</span>
  </div>
</section>

</body>
</html>
```